Welcome Card Banner Desing for email suscriptors

to get involved on this task please check my site tuvelisora.app
I wish for this task a welcome postal card to get subscribers for the newsletter and get a Coupon Code for discounts,
Keep in mind Velisora is a platform where customers (girls) can get any fashion high-end accessories ready to wear, to see the categories please visit our shop.

Target Market(s)

World wide people between 18-60 years old

Industry/Entity Type

Fashion

Coding

Coded - Design and coding required

Number of Pages Required

1 page

Font styles to use
Sans Serif

Colors
a64599
ffffff
ffc214
faa54b

Requirements
Must have
• Simplicity
• to get involved on this task please check my site tuvelisora.app
• I wish for this task a welcome postal card to get subscribers for the newsletter and get a Coupon Code for discounts,
• Keep in mind Velisora is a platform where customers (girls) can get any fashion high-end accessories ready to wear, to see the categories please visit our shop.
Nice to have
• Field for customer fill an email or just skip the banner
Should not have
• Bad grammar

```html
<!DOCTYPE html>
<html lang="en">
<head>
<meta charset="UTF-8">
<title>Welcome Postal Card – Newsletter Subscription</title>
<link rel="stylesheet" href="https://fonts.googleapis.com/css2?family=Poppins:wght@300;700;800&display=swap">
<style>
  :root {
    --page-bg: #e6e6e6;
    --purple-deep: #7f1a67;
    --purple-main: #a64599;
    --purple-light: #b23a9c;
    --purple-fold: #6b1457;
    --ribbon-orange: #eeaa2e;
    --ring-orange: #f0a52c;
    --accent-yellow: #ffc214;
    --white: #ffffff;
    --ink: #232323;
    --button-dark: #474747;
    --button-edge: #6a6a6a;
    --text-purple: #a0319a;
  }
  html, body {
    margin: 0;
    width: 1200px;
    height: 1200px;
    overflow: hidden;
    background: var(--page-bg);
  }
  .welcome-card {
    position: absolute;
    left: 49px;
    top: 243px;
    width: 1102px;
    height: 713px;
    display: block;
  }
  .ribbon-title {
    font-family: "Poppins", sans-serif;
    font-weight: 300;
    fill: var(--ink);
  }
  .ribbon-line {
    font-family: "Poppins", sans-serif;
    font-weight: 800;
  }
  .ribbon-line--white { fill: var(--white); }
  .ribbon-line--purple { fill: var(--text-purple); }
  .cta-label {
    font-family: "Poppins", sans-serif;
    font-weight: 800;
    fill: var(--accent-yellow);
  }
  .title-rule { stroke: var(--white); stroke-width: 1.2; }
  .photo-ring { fill: none; stroke: #ffffff; stroke-opacity: 0.5; stroke-width: 1; }
</style>
</head>
<body>
<svg class="welcome-card" viewBox="0 0 612 396" xmlns="http://www.w3.org/2000/svg">
  <defs>
    <radialGradient id="cardBackdrop" cx="50%" cy="60%" r="70%">
      <stop offset="0%" stop-color="#b23a9c"/>
      <stop offset="60%" stop-color="#a64599"/>
      <stop offset="100%" stop-color="#7f1a67"/>
    </radialGradient>
    <linearGradient id="modelPhotoTone" x1="0" y1="0" x2="1" y2="1">
      <stop offset="0%" stop-color="#f1ece6"/>
      <stop offset="45%" stop-color="#e6d8c8"/>
      <stop offset="75%" stop-color="#8a6a52"/>
      <stop offset="100%" stop-color="#2a2626"/>
    </linearGradient>
    <radialGradient id="bagPhotoTone" cx="50%" cy="58%" r="55%">
      <stop offset="0%" stop-color="#d9aeaa"/>
      <stop offset="45%" stop-color="#ecd3d0"/>
      <stop offset="100%" stop-color="#ffffff"/>
    </radialGradient>
    <radialGradient id="welcomeArtTone" cx="50%" cy="50%" r="55%">
      <stop offset="0%" stop-color="#ecd391"/>
      <stop offset="55%" stop-color="#f8ecd0"/>
      <stop offset="100%" stop-color="#ffffff"/>
    </radialGradient>
  </defs>

  <rect class="card-backdrop" width="612" height="396" fill="url(#cardBackdrop)"/>

  <g class="feature-model">
    <circle class="photo-ring" cx="120" cy="130" r="77"/>
    <circle cx="120" cy="130" r="72" fill="url(#modelPhotoTone)" role="img" aria-label="Photo of a smiling woman in a brown hat wearing a black top and long pendant necklace"/>
  </g>

  <g class="welcome-emblem">
    <circle cx="303" cy="103" r="96" fill="var(--ring-orange)"/>
    <circle cx="303" cy="103" r="84" fill="url(#welcomeArtTone)" role="img" aria-label="Hand-lettered Welcome! script surrounded by gold and black stars"/>
  </g>

  <g class="feature-product">
    <circle class="photo-ring" cx="485" cy="130" r="77"/>
    <circle cx="485" cy="130" r="72" fill="url(#bagPhotoTone)" role="img" aria-label="Photo of a pink leather tote bag with matching pouch and scarf"/>
  </g>

  <g class="headline-ribbon">
    <polygon class="ribbon-fold" points="26,228 46,217 46,312 30,312" fill="var(--purple-fold)"/>
    <polygon class="ribbon-fold" points="586,228 566,217 566,312 582,312" fill="var(--purple-fold)"/>
    <polygon class="ribbon-band" points="46,217 566,217 573,327 35,327" fill="var(--ribbon-orange)"/>

    <g class="title-rules">
      <line class="title-rule" x1="68" y1="238" x2="146" y2="238"/>
      <line class="title-rule" x1="80" y1="241.5" x2="146" y2="241.5"/>
      <line class="title-rule" x1="92" y1="245" x2="146" y2="245"/>
      <line class="title-rule" x1="456" y1="238" x2="538" y2="238"/>
      <line class="title-rule" x1="456" y1="241.5" x2="526" y2="241.5"/>
      <line class="title-rule" x1="456" y1="245" x2="514" y2="245"/>
    </g>

    <text class="ribbon-title" x="301" y="250" font-size="23" text-anchor="middle" textLength="298" lengthAdjust="spacingAndGlyphs">Welcome Postal Card</text>
    <text class="ribbon-line ribbon-line--white" x="301" y="278" font-size="19.5" text-anchor="middle" textLength="474" lengthAdjust="spacingAndGlyphs">TO GET SUBSCRIBERS FOR THE NEWSLETTER</text>
    <text class="ribbon-line ribbon-line--purple" x="301" y="305" font-size="19.5" text-anchor="middle" textLength="469" lengthAdjust="spacingAndGlyphs">AND GET A COUPON CODE FOR DISCOUNTS</text>
  </g>

  <g class="cta-button">
    <rect x="141" y="319" width="329" height="56" fill="var(--button-dark)"/>
    <rect x="143.5" y="321.5" width="324" height="51" fill="none" stroke="var(--button-edge)" stroke-width="1"/>
    <polygon class="cta-arrow" points="158,337 178,347 158,357" fill="var(--accent-yellow)"/>
    <text class="cta-label" x="188" y="355.5" font-size="24">SUBSCRIBE NOW</text>
  </g>
</svg>
</body>
</html>
```